Bright Meadow Lodge website (design only)

Bright Meado Lodge (http://www.brightmeadowmw.example) is a private Safari lodge located in Malawi.
We would like a modern, professional website designed that does not subscribe to the cliched view of a Safari in Africa, but still maintain a wildlife/safari atmosphere.

The aim of our website is to entice people & drive them to the booking form.

Here are some examples of websites that we like. Although we would like our site to be a bit more in line with modern web design trends.

http://www.korumelo.example/
http://www.tarvonel.example/
http://www.plovandetri.example/

Requirements
Must have
• Here is a list of the pages required. Most of them will follow a standard content layout. I.e. heading, body and images.

If you take a look at the website, you will get an idea of hoe many page types there are +- 5

http://www.brightmeadowmw.example/index.htm

About Bright Meadow
Ulkoro Country Club
Rooms
Conferences
Cuisine
Facilities
Your Safari
Activities
Rates & Special Offers
Booking form
Latest Developments
How To Get There
Gallery
Contact Us
Blog / Newsfeed

```html
<!DOCTYPE html>
<html lang="en">
<head>
<meta charset="utf-8">
<title>Bright Meadow Lodge</title>
<link rel="stylesheet" href="https://fonts.googleapis.com/css2?family=Jost:wght@400;500;600&family=Arimo:wght@400&family=Cormorant+Garamond:ital,wght@1,500&display=swap">
<style>
  :root {
    --page: #262626;
    --nav-bar: #1c1c1c;
    --nav-active: #0e0e0e;
    --gold: #c9a663;
    --gold-soft: #b9a27a;
    --body-text: #c9c1ae;
    --nav-text: #f2efe8;
    --rule: #3b3b3b;
    --frame: #d9d4c7;
    --footer: #3c3c31;
    --footer-text: #b7b39f;
    --icon: #9c968a;
  }
  * { margin: 0; padding: 0; box-sizing: border-box; }
  html, body { width: 1200px; height: 972px; overflow: hidden; background: var(--page); }
  body { position: relative; font-family: "Arimo", Arial, sans-serif; }

  .site-header { position: absolute; left: 0; top: 0; width: 1200px; height: 103px; }
  .brand { position: absolute; left: 42px; top: 30px; display: flex; align-items: baseline; gap: 28px; }
  .brand-name { font-family: "Jost", sans-serif; font-weight: 500; font-size: 35px; color: var(--gold); letter-spacing: 0.2px; }
  .brand-location { font-family: "Jost", sans-serif; font-weight: 500; font-size: 13.5px; color: var(--gold); }

  .social { position: absolute; left: 978px; top: 0; display: flex; }
  .social-item { width: 46px; height: 30px; border-left: 1px solid #4a4a4a; display: flex; align-items: center; justify-content: center; }
  .social-item:last-child { border-right: 1px solid #4a4a4a; }

  .main-nav { position: absolute; left: 40px; top: 103px; width: 1121px; height: 37px; background: var(--nav-bar); display: flex; }
  .main-nav a { display: block; padding: 0 8px; line-height: 37px; font-size: 13.6px; color: var(--nav-text); text-decoration: none; white-space: nowrap; }
  .main-nav a.is-active { background: var(--nav-active); }

  .hero { position: absolute; left: 36px; top: 141px; width: 1125px; height: 357px;
    background: linear-gradient(180deg, #8a5a1e 0%, #e0a344 16%, #f3cf83 30%, #e9c06c 42%, #d7a64d 62%, #c08a3a 100%); }
  .hero-tagline { position: absolute; right: 28px; top: 196px; font-family: "Cormorant Garamond", serif; font-style: italic; font-weight: 500; font-size: 27px; color: #4a3a22; letter-spacing: 1px; }

  .features { position: absolute; left: 36px; top: 526px; width: 1125px; height: 240px; }
  .feature { position: absolute; top: 0; width: 250px; }
  .feature + .feature::before { content: ""; position: absolute; left: -21px; top: 0; width: 1px; height: 240px; background: var(--rule); }
  .thumb { width: 250px; height: 96px; border: 2px solid var(--frame); }
  .feature h2, .info h2 { font-family: "Jost", sans-serif; font-weight: 600; font-size: 13.5px; color: var(--gold); text-transform: uppercase; margin-top: 20px; letter-spacing: 0.2px; }
  .feature p, .info p { font-size: 12px; line-height: 16.2px; color: var(--body-text); margin-top: 3px; }

  .info { position: absolute; top: 806px; width: 260px; }
  .info h2 { margin-top: 0; }
  .info-divider { position: absolute; left: 306px; top: 812px; width: 1px; height: 82px; background: var(--rule); }

  .booking-cta { position: absolute; left: 617px; top: 807px; width: 544px; height: 100px; border: 2px solid var(--frame);
    background: linear-gradient(180deg, #4b4a1e 0%, #8b7a34 45%, #a78a46 70%, #4d4a2a 100%); }
  .booking-cta span { position: absolute; right: 26px; bottom: 6px; font-family: "Cormorant Garamond", serif; font-style: italic; font-weight: 500; font-size: 25px; color: #f4efe2; letter-spacing: 1px; }

  .site-footer { position: absolute; left: 0; top: 945px; width: 1200px; height: 27px; background: var(--footer); }
  .site-footer p { position: absolute; right: 39px; top: 7px; font-size: 11px; color: var(--footer-text); }
</style>
</head>
<body>
  <header class="site-header">
    <div class="brand">
      <span class="brand-name">Bright Meadow Lodge</span>
      <span class="brand-location">Tolvane Estate | Marundi</span>
    </div>
    <div class="social">
      <div class="social-item"><svg width="14" height="14"><circle cx="7" cy="7" r="6" fill="var(--icon)"/></svg></div>
      <div class="social-item"><svg width="14" height="14"><circle cx="7" cy="7" r="6" fill="var(--icon)"/></svg></div>
      <div class="social-item"><svg width="14" height="14"><circle cx="7" cy="7" r="6" fill="var(--icon)"/></svg></div>
      <div class="social-item"><svg width="16" height="12" aria-label="Email"><rect x="0.5" y="0.5" width="15" height="11" fill="var(--icon)"/><path d="M1 1 L8 7 L15 1" fill="none" stroke="var(--page)" stroke-width="1.4"/></svg></div>
    </div>
  </header>

  <nav class="main-nav">
    <a class="is-active" href="#">Home</a>
    <a href="#">About</a>
    <a href="#">Gallery</a>
    <a href="#">Safari</a>
    <a href="#">Activities</a>
    <a href="#">Rooms</a>
    <a href="#">Cuisine</a>
    <a href="#">Conferences</a>
    <a href="#">Facilities</a>
    <a href="#">Rates &amp; Specials</a>
    <a href="#">Bookings</a>
    <a href="#">Developments</a>
    <a href="#">How To Get There</a>
    <a href="#">Blog</a>
    <a href="#">Contact Us</a>
  </nav>

  <section class="hero" role="img" aria-label="Zebras walking through golden grassland under a setting sun">
    <p class="hero-tagline">...experience nature in it's element</p>
  </section>

  <section class="features">
    <article class="feature" style="left:0">
      <div class="thumb" role="img" aria-label="Two zebras side by side" style="background:linear-gradient(90deg,#d9d6cf,#3a3632 50%,#e4e1da)"></div>
      <h2>Bright Meadow Lodge</h2>
      <p>Warmest welcome to the unique Malawi experience: lodge complex, game park, the 18 hole Ulkoro golf club &amp; Senna dam. Bright Meadow Lodge provides all the holiday and business prerequisites in a beautiful, relaxing, quiet and secure environment.</p>
    </article>
    <article class="feature" style="left:290px">
      <div class="thumb" role="img" aria-label="Two antelope in the bush" style="background:linear-gradient(90deg,#5c6b2e,#a3642c 45%,#c8874a 70%,#6d7a3a)"></div>
      <h2>Game &amp; Wild Birds</h2>
      <p>Lorem ipsum dolor sit amet, consectetuer adipiscing elit, sed diam nonummy nibh euismod tincidunt ut laoreet dolore magna aliquam erat volutpat. Ut wisi enim ad minim veniam quis nostrud exerci tatin ullamcorper suscipit lobortis nisl ut aliquip ex ea comod.</p>
    </article>
    <article class="feature" style="left:581px">
      <div class="thumb" role="img" aria-label="Lodge lounge with red sofas and wooden table" style="background:linear-gradient(180deg,#8a6a3e,#9b2424 50%,#5a2a1a)"></div>
      <h2>The Lodge &amp; Rooms</h2>
      <p>Lorem ipsum dolor sit amet, consectetuer adipiscing elit, sed diam nonummy nibh euismod tincidunt ut laoreet dolore magna aliquam erat volutpat. Ut wisi enim ad minim veniam quis nostrud exerci tatin ullamcorper suscipit lobortis nisl ut aliquip ex ea comod.</p>
    </article>
    <article class="feature" style="left:871px">
      <div class="thumb" role="img" aria-label="Conference hall with dressed tables" style="background:linear-gradient(180deg,#d8d2c8,#8a2a3a 55%,#6a3a2a)"></div>
      <h2>Conference &amp; Resturant</h2>
      <p>Lorem ipsum dolor sit amet, consectetuer adipiscing elit, sed diam nonummy nibh euismod tincidunt ut laoreet dolore magna aliquam erat volutpat. Ut wisi enim ad minim veniam quis nostrud exerci tatin ullamcorper suscipit lobortis nisl ut aliquip ex ea comod.</p>
    </article>
  </section>

  <section class="info" style="left:36px">
    <h2>Bright Meadow Activities</h2>
    <p>18 Hole Golf Course, Guided Walks, Game Drives, Bird Watching, Fishing, Sailing, Swimming Pool, Bushwalking, Hiking, and Trekking.</p>
  </section>
  <div class="info-divider"></div>
  <section class="info" style="left:331px">
    <h2>Safari Wildlife</h2>
    <p>Giraffe, Sable and their newbord calves, Waterbuck, Zebra, Impala, Wildebeest, Nyala and numerous duiker and smaller wild cats and otter</p>
  </section>

  <a class="booking-cta" href="#" role="img" aria-label="Herd of impala drinking at a waterhole"><span>...enquire for a booking</span></a>

  <footer class="site-footer">
    <p>2012 © www.brightmeadowmw.example | All rights reserved</p>
  </footer>
</body>
</html>
```